Lose Up To 1 LB Of Fat Per Day

We need a double sided street sign for our weight loss clinic. We need the doctors picture to the right side of the sign and we need a challenge “Lose Up To 1 Pound Of Fat Per Day” included in the signage.
Our color scheme for the clinic are black, white, teal and silver.
The phone number should be at the bottom of the sign
555-206–3948

Target Market(s)

Weight Loss

Font styles to use
Sans Serif

```html
<!DOCTYPE html>
<html lang="en">
<head>
<meta charset="utf-8">
<title>Weight Loss Program Street Sign</title>
<link href="https://fonts.googleapis.com/css2?family=Anton&family=Poppins:wght@400;500;700&display=swap" rel="stylesheet">
<style>
  :root {
    --teal: #468d82;
    --teal-bright: #1f9e8c;
    --black: #111111;
    --white: #ffffff;
    --silver: #e3e4e6;
    --page: #f2f2f2;
    --suit: #2a2c31;
    --skin: #d9a98f;
  }
  * { margin: 0; padding: 0; box-sizing: border-box; }
  html, body { width: 920px; height: 1200px; overflow: hidden; background: var(--page); }
  .canvas { position: relative; width: 920px; height: 1200px; }
  .sign {
    position: absolute; left: 20px; top: 380px;
    width: 880px; height: 440px;
    background: var(--white);
    box-shadow: 0 4px 14px rgba(0,0,0,0.25);
    overflow: hidden;
  }
  .headline-line { position: absolute; left: 29px; white-space: nowrap; line-height: 1; }
  .headline-lose {
    top: 22px; font-family: "Poppins", sans-serif; font-weight: 700;
    font-size: 63px; color: var(--teal); letter-spacing: -1px;
  }
  .headline-pound {
    top: 96px; font-family: "Anton", sans-serif;
    font-size: 76px; color: var(--black); letter-spacing: 0.5px;
  }
  .headline-day {
    top: 175px; font-family: "Anton", sans-serif;
    font-size: 110px; color: var(--teal); letter-spacing: 1px;
  }
  .disclaimer {
    position: absolute; left: 29px; top: 299px;
    font-family: "Poppins", sans-serif; font-weight: 400;
    font-size: 13.5px; line-height: 1.05; color: #333;
  }
  .doctor-photo {
    position: absolute; left: 512px; top: 25px; width: 288px; height: 415px;
    background: linear-gradient(180deg, var(--skin) 0%, var(--skin) 28%, var(--suit) 40%, var(--suit) 100%);
    border-radius: 120px 120px 0 0;
  }
  .brand {
    position: absolute; left: 690px; top: 40px;
    display: flex; align-items: center; gap: 8px;
  }
  .brand-dot { width: 14px; height: 14px; border-radius: 50%; background: var(--teal-bright); }
  .brand-name {
    font-family: "Poppins", sans-serif; font-weight: 500; color: var(--teal-bright);
    font-size: 15px; line-height: 1.15; letter-spacing: 1px;
  }
  .bands { position: absolute; left: 0; top: 333px; width: 880px; height: 77px; }
  .phone {
    position: absolute; left: 29px; top: 333px; height: 77px;
    display: flex; align-items: center; gap: 20px;
  }
  .phone-number {
    font-family: "Anton", sans-serif; font-size: 44px; color: var(--white);
    letter-spacing: 3px; line-height: 1;
  }
  .program {
    position: absolute; left: 500px; top: 333px; width: 330px; height: 77px;
    display: flex; flex-direction: column; justify-content: center; align-items: center;
    font-family: "Poppins", sans-serif; font-weight: 700; font-size: 20px;
    color: var(--white); letter-spacing: 0.8px; line-height: 1.25;
  }
</style>
</head>
<body>
<div class="canvas">
  <div class="sign">
    <div class="doctor-photo" role="img" aria-label="Photo of the doctor in a dark suit and purple tie, hands clasped"></div>

    <div class="brand">
      <span class="brand-dot"></span>
      <span class="brand-name">EVERLINE<br>HEALTH CENTERS</span>
    </div>

    <div class="headline-line headline-lose">LOSE UP TO</div>
    <div class="headline-line headline-pound">1 POUND OF FAT</div>
    <div class="headline-line headline-day">PER DAY!</div>

    <p class="disclaimer">patients results may vary depending on starting weight,<br>adherence to the program and the variety of the factors.</p>

    <svg class="bands" viewBox="0 0 880 77" aria-hidden="true">
      <polygon points="0,0 454,0 482,77 0,77" fill="var(--teal-bright)"/>
      <polygon points="466,0 818,0 849,77 500,77" fill="var(--black)"/>
    </svg>

    <div class="phone">
      <svg width="32" height="32" viewBox="0 0 32 32" aria-hidden="true">
        <circle cx="16" cy="16" r="14" fill="none" stroke="var(--white)" stroke-width="3"/>
        <path d="M11 9 l3 0 l1.5 4 l-2 1.5 c1 2 2.5 3.5 4.5 4.5 l1.5 -2 l4 1.5 l0 3 c0 1 -1 2 -2 2 c-6 -0.5 -11 -5.5 -11.5 -11.5 c0 -1 1 -2 2 -2z" fill="var(--white)"/>
      </svg>
      <span class="phone-number">555-206–3948</span>
    </div>

    <div class="program">
      <span>DR. MARTIN HALVERS</span>
      <span>WEIGHT LOSS PROGRAM</span>
    </div>
  </div>
</div>
</body>
</html>
```